The Pixel Tavern Business card.

A Simple card with our Logo and contact information. To give to investors and other professionals.

We are a nerd themed bar.
our target market is young professionals age 21+ but the real purpose of this business card is to present to potential investors and other professionals with our contact information. as we are still looking for funding before we start up.

I am partial to green and my partner likes red we are open to iteration.

Target Market(s)

Investors

Industry/Entity Type

Business

Contact Information for Business Card

Marcus Henley (555) 730-6621 kent.w4100@mailbox-demo.net Brian Tolle (555) 918-2047 briant731@mailbox-demo.net

Font styles to use
Serif

Requirements
Nice to have
• Keep it simple but not boring.
• Use the Logos but feel free to edit them to match theme/colors.
• Keep the back clean and use one of the Logos.

```html
<!DOCTYPE html>
<html lang="en">
<head>
<meta charset="utf-8">
<title>The Pixel Tavern – Business Card</title>
<link rel="stylesheet" href="https://fonts.googleapis.com/css2?family=PT+Sans:wght@400;700&display=swap">
<style>
  :root {
    --backdrop: #2b2b2b;
    --card: #141414;
    --card-edge: #0b0b0b;
    --text-light: #e9e9e9;
    --accent-green: #52b947;
    --divider: #2f2f2f;
  }
  * { margin: 0; padding: 0; box-sizing: border-box; }
  html, body {
    width: 1200px;
    height: 900px;
    overflow: hidden;
    background: var(--backdrop);
    font-family: "PT Sans", sans-serif;
  }
  .canvas {
    position: relative;
    width: 1200px;
    height: 900px;
    display: flex;
    align-items: center;
    justify-content: center;
    gap: 50px;
  }
  .card {
    position: relative;
    width: 525px;
    height: 300px;
    background: var(--card);
    border-radius: 22px;
    box-shadow: 0 1px 0 var(--card-edge);
    overflow: hidden;
  }
  /* Front */
  .card-front { display: flex; }
  .brand-panel {
    width: 58%;
    display: flex;
    align-items: center;
    justify-content: center;
  }
  .brand-name {
    color: var(--text-light);
    font-weight: 700;
    text-transform: uppercase;
    text-align: center;
    line-height: 1;
  }
  .brand-name .brand-small { display: block; font-size: 15px; letter-spacing: 1px; }
  .brand-name .brand-main { display: block; font-size: 30px; letter-spacing: 1px; margin: 2px 0 4px; }
  .brand-name .brand-tagline { display: block; font-size: 9px; letter-spacing: 1.5px; }
  .divider {
    width: 1px;
    background: var(--divider);
    margin: 40px 0;
  }
  .contact-panel {
    flex: 1;
    display: flex;
    flex-direction: column;
    justify-content: center;
    gap: 16px;
    padding-left: 18px;
  }
  .contact-name {
    color: var(--accent-green);
    font-weight: 700;
    font-size: 17px;
    margin-bottom: 3px;
  }
  .contact-line {
    display: flex;
    align-items: center;
    gap: 8px;
    color: var(--text-light);
    font-size: 12.5px;
    line-height: 1.45;
  }
  .contact-line svg { width: 9px; height: 9px; flex: none; fill: var(--accent-green); }
  /* Back */
  .card-back {
    display: flex;
    align-items: center;
    justify-content: center;
  }
  .back-brand {
    display: flex;
    align-items: center;
    gap: 14px;
    color: var(--text-light);
    font-weight: 700;
    font-size: 26px;
    letter-spacing: 1px;
    text-transform: uppercase;
  }
  .back-dot {
    width: 18px;
    height: 18px;
    border-radius: 50%;
    background: var(--accent-green);
  }
</style>
</head>
<body>
<main class="canvas">
  <section class="card card-front">
    <div class="brand-panel">
      <div class="brand-name">
        <span class="brand-small">The</span>
        <span class="brand-main">Pixel Tavern</span>
        <span class="brand-tagline">Lounge and Arcade</span>
      </div>
    </div>
    <div class="divider"></div>
    <div class="contact-panel">
      <div class="contact">
        <p class="contact-name">Marcus Henley</p>
        <p class="contact-line">
          <svg viewBox="0 0 10 10" aria-hidden="true"><path d="M2 0.5 L3.6 2.6 L2.7 3.6 Q3.8 5.9 6.3 7.3 L7.3 6.3 L9.5 7.9 L8.4 9.5 Q3.7 8.8 0.5 1.6 Z"/></svg>
          (555) 730-6621
        </p>
        <p class="contact-line">
          <svg viewBox="0 0 10 10" aria-hidden="true"><path d="M0.5 2 H9.5 V8 H0.5 Z M1 2.4 L5 5.4 L9 2.4 V2.3 H1 Z" fill-rule="evenodd"/></svg>
          kent.w4100@mailbox-demo.net
        </p>
      </div>
      <div class="contact">
        <p class="contact-name">Brian Tolle</p>
        <p class="contact-line">
          <svg viewBox="0 0 10 10" aria-hidden="true"><path d="M2 0.5 L3.6 2.6 L2.7 3.6 Q3.8 5.9 6.3 7.3 L7.3 6.3 L9.5 7.9 L8.4 9.5 Q3.7 8.8 0.5 1.6 Z"/></svg>
          (555) 918-2047
        </p>
        <p class="contact-line">
          <svg viewBox="0 0 10 10" aria-hidden="true"><path d="M0.5 2 H9.5 V8 H0.5 Z M1 2.4 L5 5.4 L9 2.4 V2.3 H1 Z" fill-rule="evenodd"/></svg>
          briant731@mailbox-demo.net
        </p>
      </div>
    </div>
  </section>

  <section class="card card-back">
    <div class="back-brand">
      <span class="back-dot" aria-hidden="true"></span>
      <span>The Pixel Tavern</span>
    </div>
  </section>
</main>
</body>
</html>
```